Striking new Advert required for Commercial Real Estate Agency

We need a a NEW newspaper advertisement for the marketing of a large commercial property (a Backpackers lodge)

Dimensions are to be width of 101mm and height of 100mm (10cms)

Our key design statement for this advert is clean, modern and minimalist design, with accents of 'HOT PINK' colour to remove it from looking too boring, perhaps in the area of the contact icons. The heirachy of the advert is outlined in the attached ADVERTISEMENT TEXT FILE.

Our company name is THE MERIDAL COLLECTIVE, and we want our brand to appear professional yet classy in it's design style (sort of like an advertising or design agency)

We have two logo options below, one more square in its layout (which we prefer) and the other more rectangular, which may be better suited for the layout. We are not adverse to the logo being reversed (white text on black), along with other key element areas such as the main advert heading and the "FOR SALE" part, and think this would be a good option.
There are two photos attached to be included in the advert.

We have attached an example of an old advert that we did, which we DID NOT LIKE, and which was for a smaller width than the one we need (it is only 65% of the width of this one). WE have also atached a file showing layout of some of our competitors adverts, which we dont think are too good either.

We are really open for ideas, but have time pressures, so please come back with any questions as soon as you can, if needed.

Thank you
Updates

Thank you for the great and diverse designs. There are a few standout options, but one style that we prefer most.

Target Market(s)

We are wanting this newspaper advertisement to attract interest from real estat e developers, investors and motel/lodge owners, along with other high nett worth individuals

Industry/Entity Type

Real Estate

Font styles to use
Serif
Sans Serif

Colors
1b1b1b
a54499
474747
fbfbfb

Requirements
Must have
• Clean modern look, predominantly monochromatic or black and white, with the hot pink accent somewhere, as mentioned above.
• All the contents of the TEXT provided, perhaps with additional space to add a little more if needed, Please advise if you think we dont have enough space for all of the TEXT
Should not have
• Script like fonts
• Cartoonish characters
• a 'cheap' look

```html
<!DOCTYPE html>
<html lang="en">
<head>
<meta charset="utf-8">
<title>Marlowe's Lodge – For Sale</title>
<link rel="stylesheet" href="https://fonts.googleapis.com/css2?family=Lato:wght@400;700&family=Montserrat:wght@500;800&display=swap">
<style>
  :root {
    --ink: #1b1b1b;
    --hot-pink: #a54499;
    --slate: #474747;
    --paper: #fbfbfb;
    --stone: #8c8c8c;
    --mist: #eeeeef;
    --page: #e6e6e4;
    --sky-top: #3f73c9;
    --sky-low: #9cbbe6;
    --foliage: #4d6a32;
  }
  * { box-sizing: border-box; margin: 0; padding: 0; }
  html, body { width: 1200px; height: 903px; overflow: hidden; }
  body {
    background: var(--page);
    font-family: "Lato", Arial, sans-serif;
    color: var(--ink);
    position: relative;
  }
  .advert {
    position: absolute;
    left: 160px; top: 20px;
    width: 880px; height: 863px;
    background: var(--paper);
    overflow: hidden;
  }
  .detail-band {
    position: absolute;
    left: 0; top: 400px; width: 880px; height: 320px;
    background: var(--mist);
  }
  .property-photo {
    position: absolute;
    left: 40px; top: 40px; width: 430px; height: 420px;
    background: linear-gradient(180deg, var(--sky-top) 0%, var(--sky-low) 45%, #d9dde2 62%, var(--foliage) 100%);
  }
  .headline-column {
    position: absolute;
    left: 492px; top: 40px; width: 350px;
  }
  .for-sale {
    display: inline-block;
    background: var(--hot-pink);
    color: #fff;
    font-family: "Montserrat", sans-serif;
    font-weight: 800;
    font-size: 56px;
    line-height: 1;
    padding: 14px 22px 12px;
    letter-spacing: 1px;
  }
  .campaign-title {
    font-size: 24px;
    color: var(--ink);
    margin: 10px 0 14px 10px;
  }
  .address-box {
    background: var(--stone);
    color: #fff;
    font-family: "Montserrat", sans-serif;
    font-weight: 500;
    font-size: 25px;
    line-height: 1.2;
    text-align: center;
    padding: 16px 12px;
    width: 320px;
    margin-left: 20px;
  }
  .teaser {
    font-size: 20px;
    line-height: 1.3;
    margin: 18px 0 0 24px;
  }
  .tender-strip {
    position: absolute;
    left: 494px; top: 372px; width: 350px;
    background: #f6f6f7;
    color: var(--hot-pink);
    font-weight: 700;
    font-size: 22px;
    padding: 14px 16px;
  }
  .key-details {
    position: absolute;
    left: 40px; top: 472px; width: 810px;
  }
  .key-details h2 {
    font-size: 24px;
    font-weight: 700;
    line-height: 1.25;
    margin-bottom: 10px;
  }
  .key-details ul { list-style: none; }
  .key-details li {
    position: relative;
    font-size: 20px;
    line-height: 1.32;
    padding-left: 34px;
    margin-bottom: 6px;
  }
  .key-details li::before {
    content: "";
    position: absolute;
    left: 8px; top: 10px;
    width: 9px; height: 9px;
    border-radius: 50%;
    background: var(--hot-pink);
  }
  .contact-bar {
    position: absolute;
    left: 0; top: 720px; width: 880px; height: 143px;
    background: var(--ink);
    color: #fff;
    padding: 26px 40px;
    display: flex;
    align-items: center;
  }
  .agent { width: 240px; flex: none; }
  .agent-name { font-size: 28px; font-weight: 700; margin-bottom: 6px; }
  .contact-line {
    display: flex; align-items: center; gap: 12px;
    font-size: 21px; line-height: 1.4;
    white-space: nowrap;
  }
  .contact-line svg { width: 20px; height: 20px; flex: none; }
  .online { width: 330px; flex: none; }
  .brand-name {
    margin-left: auto;
    align-self: flex-end;
    margin-bottom: 6px;
    font-family: "Lato", Arial, sans-serif;
    font-weight: 700;
    font-size: 16px;
    letter-spacing: 0.5px;
    color: #fff;
    white-space: nowrap;
  }
</style>
</head>
<body>
  <article class="advert">
    <div class="detail-band"></div>

    <div class="property-photo" role="img" aria-label="Photo of the two-storey white weatherboard lodge with balconies, garden shrubs and blue sky"></div>

    <header class="headline-column">
      <div class="for-sale">FOR SALE</div>
      <p class="campaign-title">Mount Victoria Land Grab</p>
      <div class="address-box">Marlowe's Lodge,<br>48 Tarrant Street,<br>Mount Victoria</div>
      <p class="teaser">This Old Beauty has served many,<br>and is now ripe for development.</p>
    </header>

    <p class="tender-strip">Now Selling by Closed Tender</p>

    <section class="key-details">
      <h2>One of Mt Vic's largest land areas, now offered with vacant possession,<br>with key details being:</h2>
      <ul>
        <li>Large Land area of 2076m² with elevated sunny position and great outlook<br>+ access from Wexley Street</li>
        <li>Existing Backpackers Lodge of 970m² providing multiple rooms with amenity areas</li>
        <li>Four adjacent sites also available, taking total land area to 4452m², an unprecedented Land Offering in this popular city fringe location</li>
      </ul>
    </section>

    <footer class="contact-bar">
      <div class="agent">
        <p class="agent-name">Glen Porter</p>
        <p class="contact-line">
          <svg viewBox="0 0 24 24" fill="none" stroke="var(--hot-pink)" stroke-width="2.2" stroke-linecap="round" stroke-linejoin="round"><path d="M5 3h4l2 5-3 2a12 12 0 0 0 6 6l2-3 5 2v4a2 2 0 0 1-2 2A17 17 0 0 1 3 5a2 2 0 0 1 2-2z"/></svg>
          (04) 555 0142
        </p>
        <p class="contact-line">
          <svg viewBox="0 0 24 24" fill="none" stroke="var(--hot-pink)" stroke-width="2.2" stroke-linecap="round"><rect x="6" y="2" width="12" height="20" rx="2"/><line x1="11" y1="18" x2="13" y2="18"/></svg>
          (021) 555 817
        </p>
      </div>
      <div class="online">
        <p class="contact-line">
          <svg viewBox="0 0 24 24" fill="none" stroke="var(--hot-pink)" stroke-width="2.2" stroke-linejoin="round"><rect x="3" y="5" width="18" height="14" rx="1"/><path d="M3 6l9 7 9-7"/></svg>
          glen@meridalcollective.co.nz
        </p>
        <p class="contact-line">
          <svg viewBox="0 0 24 24" fill="none" stroke="var(--hot-pink)" stroke-width="2"><circle cx="12" cy="12" r="9"/><path d="M3 12h18M12 3c3 3 3 15 0 18M12 3c-3 3-3 15 0 18"/></svg>
          www.meridalcollective.co.nz
        </p>
      </div>
      <p class="brand-name">THE MERIDAL COLLECTIVE</p>
    </footer>
  </article>
</body>
</html>
```